Visitenkarten-Design für Immobilienmakler
Zielgruppe
Immobilienmakler
Aufgabenstellung
Top moderne hochwertige Visitenkate, wir hätten gerne eine sehr hochwertig moderne Visitenkarte mit Bild vom Mitarbeiter... Anbei habe ich die alte Visitenkarte die ich sehr kindlich finde... Es sollte jetzt sehr exklusive aussehen. Alle Daten können von der alten Visitenkarte übernommen werden.. danke

```html
<!DOCTYPE html>
<html lang="de">
<head>
<meta charset="utf-8">
<title>Velmar Agentur – Visitenkarte</title>
<link rel="stylesheet" href="https://fonts.googleapis.com/css2?family=Noto+Serif:wght@400;700&display=swap">
<style>
  :root {
    --stage: #c9c9cc;
    --card-dark: #15171b;
    --card-light: #ffffff;
    --brand-green: #0f8a45;
    --ink: #2a2a2a;
    --rule: #1c1c1c;
    --photo-tone: #d9dde2;
    --name-light: #f2f2f2;
  }
  * { margin: 0; padding: 0; box-sizing: border-box; }
  html, body {
    width: 1200px; height: 786px; overflow: hidden;
    background: var(--stage);
  }
  .stage {
    position: relative; width: 1200px; height: 786px;
    display: flex; align-items: center; justify-content: center; gap: 54px;
  }
  .card {
    position: relative; width: 520px; height: 336px;
    box-shadow: 0 10px 28px rgba(0,0,0,.18);
    overflow: hidden;
  }
  /* Front */
  .card--front {
    background: var(--card-dark);
    display: flex; align-items: center; justify-content: center;
  }
  .front__name {
    font-family: "Noto Serif", serif; font-weight: 700;
    font-size: 38px; color: var(--name-light); letter-spacing: .5px;
  }
  /* Back */
  .card--back { background: var(--card-light); }
  .back__rule {
    position: absolute; top: 86px; height: 3px; background: var(--rule);
  }
  .back__rule--left { left: 0; width: 200px; }
  .back__rule--right { right: 0; width: 190px; }
  .back__photo {
    position: absolute; left: 225px; top: 48px;
    width: 70px; height: 70px; border-radius: 50%;
    background: radial-gradient(circle at 50% 40%, #eef0f3, var(--photo-tone));
  }
  .back__person {
    position: absolute; left: 0; right: 0; top: 128px;
    text-align: center; font-family: "Noto Serif", serif; color: var(--ink);
  }
  .person__name {
    font-weight: 700; font-size: 22px; color: var(--brand-green);
    letter-spacing: .5px; line-height: 1.1;
  }
  .person__role, .person__email { font-size: 13px; line-height: 1.35; }
  .person__role { font-weight: 700; color: #444; }
  .back__band {
    position: absolute; left: 0; right: 0; bottom: 0; height: 98px;
    background: var(--brand-green);
    display: flex; flex-direction: column; justify-content: center;
    text-align: center; font-family: "Noto Serif", serif;
    font-size: 12.5px; line-height: 1.6; color: #ffffff;
  }
  .back__band strong { font-weight: 700; }
</style>
</head>
<body>
<main class="stage">
  <section class="card card--front" aria-label="Vorderseite">
    <p class="front__name">Velmar Agentur</p>
  </section>

  <section class="card card--back" aria-label="Rückseite">
    <div class="back__rule back__rule--left"></div>
    <div class="back__rule back__rule--right"></div>
    <div class="back__photo" role="img" aria-label="Porträtfoto des Mitarbeiters"></div>
    <div class="back__person">
      <p class="person__name">LUKAS BERGER</p>
      <p class="person__role">Dipl. Immobilienmanager / Geschäftsführer</p>
      <p class="person__email">lukas@velmar-agentur.com</p>
    </div>
    <div class="back__band">
      <p><strong>Velmar Agentur Berger GmbH</strong> • Am Anger 12 • AT - 6850 Dornbirn</p>
      <p><strong>Fon</strong> +43 5500 10 200 30 • <strong>Fax</strong> +43 660 000 4812</p>
      <p>office@velmar-agentur.com • www.velmar-agentur.com</p>
    </div>
  </section>
</main>
</body>
</html>
```